Modern Catering Company needs Letterhead Design

We need a letterhead design that will make effective use of the corporate logo and color scheme, along with careful typography, helps this letterhead design communicate the brand well. We do have a corporate logo, however feel free to enhance the color scheme with gold and purple. We are serving a very upscale clientele so the letterhead has to reflect elegance, professionalism, cleanliness, and modern style. We are branding the company so the letterhead and business cards must fit the brand story. There should be no cartoonish elements in the design and we are looking for sharper lines.

Target Market(s)

Businesses and upscale clientele

Industry/Entity Type

Catering

Contact Information for Business Card

while this design can have any number of quirks and distinctions, it needs to be cohesive with the entire brand story clean, professional but edgy

Requirements
Must have
• must have good and carefully placement of it’s logo and where you place the text or the message. Colors blue, very deep purple, jewel tones not pastels, gold. Blue must be the primary color you may accent with purple or gold. Contact information is as follows: Co-Owners/ Chefs: R. Hollowmere & L. Brandt, phone: 414-555-0182 email:Contact@orchardtablecatering.example, address: 6127 W Larkspur Hollow Rd, Milwaukee, WI 53299
Should not have
• pastel colors, Do not add the BBQ information to the letterhead or business card it was a mistake by the previous designer.

```html
<!DOCTYPE html>
<html lang="en">
<head>
<meta charset="utf-8">
<title>Orchard Table Catering – Business Card</title>
<link rel="stylesheet" href="https://fonts.googleapis.com/css2?family=Source+Sans+3:wght@400;600&display=swap">
<style>
  :root {
    --backdrop: #4a4a4a;
    --card-blue: #0f2457;
    --card-blue-deep: #0a1a40;
    --gold: #f0c13f;
    --gold-deep: #d9a531;
    --gold-light: #fbe27a;
    --purple: #a58be0;
    --text-light: #f2f2f2;
    --rule: #cfcfcf;
    --back-text: #1b2f66;
    --back-brand: #0f2457;
  }
  * { margin: 0; padding: 0; box-sizing: border-box; }
  html, body {
    width: 1105px; height: 1200px; overflow: hidden;
    background: var(--backdrop);
    font-family: "Source Sans 3", "Myriad Pro", sans-serif;
  }
  .canvas { position: relative; width: 1105px; height: 1200px; }

  .card {
    position: absolute; left: 196px; width: 720px; height: 412px;
    box-shadow: 0 3px 10px rgba(0,0,0,.45);
    overflow: hidden;
  }
  .card--front {
    top: 146px;
    background: linear-gradient(160deg, var(--card-blue) 0%, var(--card-blue-deep) 100%);
  }
  .card--back {
    top: 602px;
    background: radial-gradient(ellipse at 50% 40%, #fdf0a0 0%, var(--gold) 55%, var(--gold-deep) 100%);
  }

  /* Front */
  .brand {
    position: absolute; right: 30px; top: 118px; text-align: right;
    color: var(--gold); font-weight: 400; line-height: 1;
  }
  .brand__name { font-size: 52px; letter-spacing: 1px; text-transform: uppercase; }
  .brand__sub { font-size: 30px; letter-spacing: 14px; text-transform: uppercase; margin-top: 6px; margin-right: -14px; }

  .person__bar { position: absolute; left: 0; top: 224px; width: 10px; height: 51px; background: var(--gold); }
  .person__name { position: absolute; left: 28px; top: 219px; font-size: 27px; font-weight: 600; color: var(--gold); line-height: 1.2; }
  .person__title { position: absolute; left: 28px; top: 253px; font-size: 19px; color: var(--purple); line-height: 1.2; }
  .person__rule { position: absolute; left: 170px; right: 30px; top: 271px; height: 1px; background: var(--rule); }

  .contact { position: absolute; left: 28px; top: 287px; list-style: none; }
  .contact__item {
    display: flex; align-items: center; gap: 10px;
    height: 27.5px; font-size: 19px; color: var(--text-light);
  }
  .contact__icon { width: 16px; height: 16px; fill: var(--gold); flex: none; }

  .address {
    position: absolute; right: 30px; top: 318px; text-align: right;
    font-size: 19px; line-height: 27.5px; color: var(--text-light); font-style: normal;
  }
  .front__band {
    position: absolute; left: 0; right: 0; bottom: 0; height: 20px;
    background: linear-gradient(90deg, var(--gold-deep), var(--gold-light) 60%, var(--gold));
  }

  /* Back */
  .back__brand {
    position: absolute; left: 0; right: 0; top: 168px; text-align: center;
    color: var(--back-brand); font-weight: 600; font-size: 38px;
    letter-spacing: 2px; text-transform: uppercase; line-height: 1.2;
  }
  .back__web {
    position: absolute; left: 0; right: 0; top: 358px; text-align: center;
    font-size: 20px; letter-spacing: 1.5px; color: var(--back-text);
  }
</style>
</head>
<body>
<main class="canvas">
  <section class="card card--front" aria-label="Business card front">
    <div class="brand">
      <div class="brand__name">Orchard Table</div>
      <div class="brand__sub">Catering</div>
    </div>

    <div class="person__bar"></div>
    <h1 class="person__name">R. Hollowmere &amp; L. Brandt</h1>
    <p class="person__title">Co-Owners/Chefs</p>
    <div class="person__rule"></div>

    <ul class="contact">
      <li class="contact__item">
        <svg class="contact__icon" viewBox="0 0 16 16" aria-hidden="true"><path d="M3.5 1l2.6 2.8-1.4 2a9 9 0 0 0 5 5l2-1.4L14.5 12l-1.8 2.6C7 14 2 9 1.4 3.2z"/></svg>
        414-555-0182
      </li>
      <li class="contact__item">
        <svg class="contact__icon" viewBox="0 0 16 16" aria-hidden="true"><path d="M1 3h14v1.2L8 8.6 1 4.2zM1 5.6l7 4.4 7-4.4V13H1z"/></svg>
        Contact@orchardtablecatering.example
      </li>
      <li class="contact__item">
        <svg class="contact__icon" viewBox="0 0 16 16" aria-hidden="true"><circle cx="8" cy="8" r="7"/><path d="M8 1.5c2 2 2 11 0 13M1.5 8h13" stroke="#0f2457" stroke-width="1.2" fill="none"/></svg>
        www.orchardtablecatering.example
      </li>
    </ul>

    <address class="address">6127 W Larkspur Hollow Rd<br>Milwaukee, WI 53299</address>
    <div class="front__band"></div>
  </section>

  <section class="card card--back" aria-label="Business card back">
    <div class="back__brand">Orchard Table Catering</div>
    <p class="back__web">www.orchardtablecatering.example</p>
  </section>
</main>
</body>
</html>
```